Global (re)insurance broker needs a business card design

We need a classic business card for our company that is headquartered in SG, with offices in Malaysia and Dubai. We specialise in insurance and reinsurance broking and consultancy for our global clients.

```html
<!DOCTYPE html>
<html lang="en">
<head>
<meta charset="utf-8">
<title>Norvale Business Card</title>
<link href="https://fonts.googleapis.com/css2?family=Poppins:ital,wght@0,400;0,500;0,600;1,700&display=swap" rel="stylesheet">
<style>
  :root {
    --brand-blue: #23449a;
    --brand-blue-deep: #1f3f92;
    --mist: #7b9ba9;
    --sage: #c2dbb3;
    --ink: #1a1d3a;
    --paper: #ffffff;
    --backdrop: #2e2e2e;
  }
  * { margin: 0; padding: 0; box-sizing: border-box; }
  html, body { width: 1200px; height: 866px; overflow: hidden; }
  body {
    background: var(--backdrop);
    font-family: "Poppins", sans-serif;
    display: flex;
    flex-direction: column;
    align-items: center;
    justify-content: center;
    gap: 40px;
  }
  .card {
    position: relative;
    width: 660px;
    height: 377px;
    overflow: hidden;
    box-shadow: 0 10px 24px rgba(0,0,0,.45);
  }
  /* Front */
  .card-front { background: var(--paper); color: var(--ink); }
  .contact { position: absolute; left: 38px; top: 44px; }
  .contact .name {
    font-weight: 700; font-style: italic; text-transform: uppercase;
    color: var(--brand-blue); font-size: 22px; letter-spacing: .5px; line-height: 1.1;
  }
  .contact .role { font-size: 17px; margin-top: 2px; }
  .rule {
    position: absolute; left: 38px; top: 108px; width: 470px; height: 1px;
    background: var(--brand-blue-deep);
  }
  .details { position: absolute; left: 38px; top: 120px; font-size: 16px; line-height: 1.35; }
  .details li { list-style: none; display: flex; align-items: center; gap: 8px; }
  .details svg { width: 16px; height: 16px; fill: var(--brand-blue); flex: none; }
  .wordmark {
    position: absolute; right: 40px; top: 150px;
    font-weight: 600; font-size: 64px; letter-spacing: 2px;
    color: var(--brand-blue); line-height: 1; white-space: nowrap;
  }
  .front-band { position: absolute; left: 0; bottom: 0; width: 660px; height: 70px; }
  .offices {
    position: absolute; right: 40px; bottom: 58px; font-size: 17px; letter-spacing: .5px;
  }
  .web {
    position: absolute; right: 40px; bottom: 10px; font-size: 17px; letter-spacing: .5px;
    color: var(--paper);
  }
  /* Back */
  .card-back {
    background: linear-gradient(205deg, var(--mist) 0%, var(--brand-blue) 45%, var(--brand-blue) 100%);
    color: var(--paper);
    display: flex; flex-direction: column; align-items: center; justify-content: center;
    text-align: center;
  }
  .card-back .wordmark-back {
    font-weight: 600; font-size: 64px; letter-spacing: 2px; line-height: 1;
  }
  .tagline { margin-top: 22px; font-size: 17px; line-height: 1.35; letter-spacing: .4px; }
</style>
</head>
<body>
  <section class="card card-front">
    <div class="contact">
      <p class="name">Mara Lindqvist</p>
      <p class="role">Chief Operating Officer</p>
    </div>
    <div class="rule"></div>
    <ul class="details">
      <li><svg viewBox="0 0 24 24"><path d="M6.6 10.8a15 15 0 0 0 6.6 6.6l2.2-2.2c.3-.3.7-.4 1-.2 1.1.4 2.3.6 3.6.6.6 0 1 .4 1 1V20c0 .6-.4 1-1 1A17 17 0 0 1 3 4c0-.6.4-1 1-1h3.5c.6 0 1 .4 1 1 0 1.3.2 2.5.6 3.6.1.3 0 .7-.2 1z"/></svg>+65 9000 1234</li>
      <li><svg viewBox="0 0 24 24"><path d="M2 5h20v14H2z M2 5l10 8 10-8" stroke="#fff" stroke-width="1.5"/></svg>mara@norvale.com</li>
    </ul>
    <p class="wordmark">NORVALE</p>
    <svg class="front-band" viewBox="0 0 660 70" preserveAspectRatio="none" aria-hidden="true">
      <path d="M0 48 L230 48 C250 48 245 30 280 30 L660 30 L660 70 L0 70 Z" fill="#23449a"/>
      <path d="M0 40 L232 40" stroke="#c2dbb3" stroke-width="7"/>
    </svg>
    <p class="offices">Singapore, Malaysia and Dubai</p>
    <p class="web">www.norvale.com</p>
  </section>

  <section class="card card-back">
    <p class="wordmark-back">NORVALE</p>
    <p class="tagline">Specialise in insurance and (Re)insurance broking<br>and consultancy for our global clients.</p>
  </section>
</body>
</html>
```